Business Card Design

Lawyer
Business name "HarlowLaw"
Areas of expertise:
property
commercial
trusts
immigration
franchising
I want the following quote on the back of the card somewhere.
"Education is when you read the fine print,
experience is what you get if you don't." Miles Corbell
Probably the "areas of expertise" should be on the back also to avoid cluttering the front.
As for colours, I like the shades of blue used on qerivo.com.
The basic part of the card with the contact info needs to be white and uncluttered.
Target Market(s)
small to medium sized self employed business people
Industry/Entity Type
Business
Contact Information for Business Card
Dennis Harlow
Phone + 64 9 517 4460
Fax: + 64 9 517 4461
PO Box 742
Clevedon
Auckland 2248
NZ
email: dennis@pinecrestlegal.co.nz

```html
<!DOCTYPE html>
<html lang="en">
<head>
<meta charset="utf-8">
<title>Dennis Harlow — Business Card</title>
<link href="https://fonts.googleapis.com/css2?family=EB+Garamond:ital,wght@0,400;0,700;1,400&family=Crimson+Pro:wght@800&display=swap" rel="stylesheet">
<style>
  :root {
    --ink-blue: #17689f;
    --card-white: #ffffff;
  }
  html, body {
    margin: 0;
    padding: 0;
    overflow: hidden;
    background: var(--card-white);
  }
  .card {
    position: relative;
    width: 1200px;
    height: 741px;
    background: var(--card-white);
    color: var(--ink-blue);
    overflow: hidden;
  }
  .card__name {
    position: absolute;
    top: 68px;
    left: 0;
    width: 100%;
    margin: 0;
    text-align: center;
    font-family: "EB Garamond", serif;
    font-weight: 700;
    font-size: 82px;
    letter-spacing: 0.2em;
    line-height: 1;
    padding-left: 0.2em;
    box-sizing: border-box;
  }
  .card__expertise {
    position: absolute;
    top: 166px;
    left: 0;
    width: 100%;
    margin: 0;
    padding: 0;
    list-style: none;
    display: flex;
    justify-content: center;
    align-items: baseline;
    font-family: "EB Garamond", serif;
    font-style: italic;
    font-size: 44px;
    line-height: 1.1;
  }
  .card__expertise li + li::before {
    content: "";
    display: inline-block;
    width: 1.5px;
    height: 0.55em;
    background: var(--ink-blue);
    margin: 0 0.2em 0 0.22em;
    vertical-align: 0.12em;
  }
  .card__quote {
    position: absolute;
    top: 356px;
    left: 80px;
    margin: 0;
    font-family: "EB Garamond", serif;
    font-style: italic;
    font-size: 33.5px;
    line-height: 1.1;
  }
  .card__quote p { margin: 0; }
  .card__quote-author {
    display: block;
    margin-top: 16px;
    font-style: italic;
  }
  .card__contact {
    position: absolute;
    top: 557px;
    left: 80px;
    margin: 0;
    font-family: "Crimson Pro", serif;
    font-weight: 800;
    font-size: 28px;
    line-height: 35px;
    font-variant-numeric: oldstyle-nums;
    font-style: normal;
  }
</style>
</head>
<body>
  <main class="card">
    <h1 class="card__name">Dennis Harlow</h1>
    <ul class="card__expertise">
      <li>property</li>
      <li>commercial</li>
      <li>trusts</li>
      <li>immigration</li>
      <li>franchising</li>
    </ul>
    <blockquote class="card__quote">
      <p>“Education is when you read the fine print, experience is what you get if you don't.”</p>
      <cite class="card__quote-author">Miles Corbell</cite>
    </blockquote>
    <address class="card__contact">
      Telephone: + 64 9 517 4460<br>
      Fax: + 64 9 517 4461<br>
      PO Box 742 Fernhollow Brackenridge 3194 NZ email: dennis@pinecrestlegal.co.nz
    </address>
  </main>
</body>
</html>
```